FRONT BUS CARD:

We were maybe thinking to have the text in a "common seal" which is an oval shape. Or CROWN VAULT underlined, then AUSTRALIA underneath...

Picture to have in the seal, or next to the words if seal not used: Gold Bars (3 of them), or scales of justice..

LOGO and pic and font to be in shiny gold.
We want 1 black background design and 1 white background design.

CROWN VAULT TRADERS

```html
<!DOCTYPE html>
<html lang="en">
<head>
<meta charset="UTF-8">
<title>Crown Vault Traders – Business Cards</title>
<link rel="stylesheet" href="https://fonts.googleapis.com/css2?family=Cinzel:wght@600&family=Jost:wght@400;600&display=swap">
<style>
  :root {
    --backdrop: #5d6c72;
    --card-black: #050505;
    --gold-light: #fbe27a;
    --gold-mid: #e3b628;
    --gold-deep: #a87a10;
    --text-white: #f4f4f4;
  }
  * { margin: 0; padding: 0; box-sizing: border-box; }
  html, body {
    width: 1200px;
    height: 960px;
    overflow: hidden;
    background: var(--backdrop);
  }
  .sheet {
    width: 1200px;
    height: 960px;
    display: flex;
    flex-direction: column;
    align-items: center;
    justify-content: center;
    gap: 60px;
  }
  .card {
    position: relative;
    width: 700px;
    height: 400px;
    padding: 12px;
    background: linear-gradient(135deg, var(--gold-light), var(--gold-mid) 40%, var(--gold-deep) 70%, var(--gold-light));
    box-shadow: 0 10px 30px rgba(0,0,0,0.35);
  }
  .card-face {
    position: relative;
    width: 100%;
    height: 100%;
    background: var(--card-black);
  }
  .brand {
    position: absolute;
    left: 0;
    right: 0;
    display: flex;
    flex-direction: column;
    align-items: center;
    font-family: "Cinzel", serif;
    font-weight: 600;
    color: var(--gold-mid);
    text-align: center;
    line-height: 1.15;
  }
  .brand-mark {
    border-radius: 50%;
    background: var(--gold-mid);
  }
  /* front */
  .card--front .brand { top: 26px; }
  .card--front .brand-mark { width: 70px; height: 70px; margin-bottom: 14px; }
  .card--front .brand-name { font-size: 20px; letter-spacing: 1px; }
  .card--front .brand-region { font-size: 14px; letter-spacing: 1px; }
  .person {
    position: absolute;
    left: 80px;
    top: 238px;
    font-family: "Jost", sans-serif;
    text-align: right;
  }
  .person-name {
    font-weight: 600;
    font-size: 26px;
    color: var(--gold-mid);
  }
  .person-role {
    font-weight: 400;
    font-size: 22px;
    color: var(--text-white);
  }
  .contacts {
    position: absolute;
    left: 360px;
    top: 212px;
    list-style: none;
    font-family: "Jost", sans-serif;
    font-size: 16px;
    color: var(--text-white);
  }
  .contacts li {
    display: flex;
    align-items: center;
    gap: 8px;
    margin-bottom: 14px;
  }
  .contacts svg { width: 14px; height: 14px; fill: var(--text-white); }
  /* back */
  .card--back .brand { top: 52px; }
  .card--back .brand-mark { width: 100px; height: 100px; margin-bottom: 20px; }
  .card--back .brand-name { font-size: 32px; letter-spacing: 1.5px; }
  .card--back .brand-region { font-size: 22px; letter-spacing: 1.5px; }
  .web {
    position: absolute;
    left: 0;
    right: 0;
    top: 300px;
    text-align: center;
    font-family: "Jost", sans-serif;
    font-size: 15px;
    letter-spacing: 0.5px;
    color: var(--gold-mid);
  }
</style>
</head>
<body>
<main class="sheet">
  <section class="card card--front" aria-label="Business card front">
    <div class="card-face">
      <div class="brand">
        <span class="brand-mark" aria-hidden="true"></span>
        <span class="brand-name">Crown Vault</span>
        <span class="brand-region">Australia</span>
      </div>
      <div class="person">
        <p class="person-name">Daniel Hart</p>
        <p class="person-role">Director</p>
      </div>
      <ul class="contacts">
        <li>
          <svg viewBox="0 0 16 16" aria-hidden="true"><path d="M4 1l2.5 3-1.5 2c1 2 3 4 5 5l2-1.5 3 2.5-1.5 2.5C8 15 1 8 1.5 2.5z"/></svg>
          <span>+ 61 400 123 456</span>
        </li>
        <li>
          <svg viewBox="0 0 16 16" aria-hidden="true"><path d="M5 1h6a1 1 0 011 1v12a1 1 0 01-1 1H5a1 1 0 01-1-1V2a1 1 0 011-1zm0 2v9h6V3z"/></svg>
          <span>+ 61 (0)2 9000 1234</span>
        </li>
        <li>
          <svg viewBox="0 0 16 16" aria-hidden="true"><path d="M1 3h14v10H1zm1.5 1.2V12h11V4.2L8 8.5z M2.8 3.8L8 7.5l5.2-3.7z"/></svg>
          <span>name@crownvault.com.au</span>
        </li>
      </ul>
    </div>
  </section>

  <section class="card card--back" aria-label="Business card back">
    <div class="card-face">
      <div class="brand">
        <span class="brand-mark" aria-hidden="true"></span>
        <span class="brand-name">Crown Vault</span>
        <span class="brand-region">Australia</span>
      </div>
      <p class="web">www.crownvault.com.au</p>
    </div>
  </section>
</main>
</body>
</html>
```